PSD website for property company

Please read the brief thoroughly.

We are looking for a new website for a property group that does property acquisitions, property development and property management.
They buy, build and lease core inner city industrial assets in Sydney, Australia.
They also invest in residential developments.

Site menu
- Home page
- Property – sub menus include – Leasing ; Projects ; Investments ; Property Management
- Capital and finance
- About
- Contact

They like this website
https://www.velmorn.com.au/

They want the site to be clean, modern and bold.
They like few colors, even black and white is OK to submit

They have a logo and style guide and useable images here:
http://www.quorvex.net/temp/PellikWeb2019.zip
The zip file is also attached to this project.
We have supplied some images to give you an idea, but we will also require you to provide at least 3 extra images from stock photos.
Use your imagination.

I am expecting a lot of similar designs, so be aware the photos you choose will be really important.
They want really 3 good stock photos used and supplied without charge.
Please not too generic, I repeat the quality of the photos is important.
You may provide several photos (but not in multiple submissions please) and we will choose the best three to be provided.

The winner will be selected on a single home page design and required to provide;
All photos use in original format without charge
A second ‘standard page’ template design based on the winning home page design

```html
<!DOCTYPE html>
<html lang="en">
<head>
<meta charset="utf-8">
<title>Pellik – Property Acquisitions, Development and Management</title>
<link rel="stylesheet" href="https://fonts.googleapis.com/css2?family=Poppins:wght@300;400;500;600&display=swap">
<style>
:root{
  --green:#516b2d;
  --green-dark:#44591f;
  --ink:#2a2a2a;
  --text:#555;
  --muted:#8a8a8a;
  --white:#fff;
  --dark:#2b2b2b;
  --dark-strip:#3a3a3a;
  --line:#dcdcdc;
}
*{box-sizing:border-box;margin:0;padding:0}
html,body{width:1200px;height:3714px;overflow:hidden}
body{position:relative;font-family:'Poppins',sans-serif;color:var(--ink);background:var(--white)}
.abs{position:absolute}
.brand{font-weight:600;letter-spacing:9px;color:var(--white);line-height:1}
.btn{position:absolute;background:var(--green);color:var(--white);font-size:14px;display:flex;align-items:center;justify-content:center;font-weight:400}
.social{display:flex;gap:7px}
.social span{width:26px;height:26px;background:var(--green);border:1px solid rgba(255,255,255,.8)}

/* hero */
.hero{left:0;top:0;width:1200px;height:635px;background:linear-gradient(180deg,#7d8795 0%,#6f7580 35%,#4b3e36 70%,#3c3a33 100%)}
.hero-shade{left:0;top:0;width:1200px;height:635px;background:rgba(40,45,60,.25)}
.nav a{position:absolute;top:35px;color:var(--white);font-size:13px;text-decoration:none}
.hero-copy{left:200px;width:800px;text-align:center;color:var(--white)}
.scroll-down{left:568px;top:603px;width:64px;height:64px;border-radius:50%;background:var(--white)}

/* shared */
.eyebrow{font-size:13px;font-weight:500;color:var(--green);text-transform:uppercase}
.h2{font-size:30px;font-weight:400;line-height:42px;color:var(--ink)}
.rule{height:2px;background:#cfd6c4;width:57px}
.body-text{font-size:12.5px;line-height:20.5px;color:var(--text);width:450px}
.photo{position:absolute}

/* services */
.services{left:0;top:1207px;width:1200px;height:622px;background:linear-gradient(90deg,#b5c3a8 0%,#c6d1bf 45%,#d9dfd9 70%,#e6ebee 100%)}
.tile{position:absolute;width:189px;height:183px;background:rgba(255,255,255,.9);text-align:center;font-size:17px;color:var(--ink)}
.tile svg{position:absolute;left:62px;top:42px}
.tile p{position:absolute;left:0;right:0;line-height:21px}

/* contact */
.field{position:absolute;border:1px solid var(--line);font-size:11px;color:var(--muted);padding:10px 14px}

/* footer */
.footnav a{position:absolute;top:3495px;color:var(--white);font-size:13px;text-decoration:none}
.info{position:absolute;color:var(--white);font-size:13px;line-height:20px}
.divider{position:absolute;top:3577px;width:1px;height:50px;background:#555}
</style>
</head>
<body>

<!-- HERO -->
<div class="abs hero" role="img" aria-label="Photo of a modern brick apartment building with trees under a cloudy sky"></div>
<div class="abs hero-shade"></div>
<div class="abs brand" style="left:140px;top:29px;font-size:31px">PELLIK</div>
<nav class="nav">
  <a style="left:443px">Home</a>
  <a style="left:513px">Property</a>
  <a style="left:600px">Capital and finance</a>
  <a style="left:764px">About Us</a>
  <a style="left:854px">Contact Us</a>
</nav>
<div class="abs social" style="left:960px;top:30px"><span></span><span></span><span></span></div>

<svg class="abs" style="left:0;top:0" width="1200" height="635">
  <polyline points="265,164 1000,164 1000,493 200,493 200,224" fill="none" stroke="#fff" stroke-width="2"/>
</svg>
<div class="abs hero-copy" style="top:246px;font-size:24px;font-weight:300">We Provide</div>
<div class="abs hero-copy" style="top:280px;font-size:32px;font-weight:500;line-height:40px">Property Acquisitions, Property Development<br>And Property Management.</div>
<div class="btn" style="left:519px;top:372px;width:160px;height:32px;font-size:16px;border:1px solid rgba(255,255,255,.6)">Contact Us Today</div>
<div class="scroll-down"></div>
<svg class="abs" style="left:592px;top:620px" width="16" height="16"><path d="M8 2v11M4 9l4 4 4-4" stroke="#555" stroke-width="1.3" fill="none"/></svg>

<!-- ABOUT -->
<svg class="abs" style="left:0;top:700px" width="600" height="470">
  <polyline points="141,38 110,38 110,461 467,461 467,437" fill="none" stroke="var(--green)" stroke-width="3"/>
</svg>
<div class="photo" style="left:141px;top:705px;width:396px;height:432px;background:linear-gradient(180deg,#e4e7ea 0%,#b9bec4 45%,#2c3340 100%)" role="img" aria-label="Photo of four smiling business people in dark suits"></div>
<div class="abs eyebrow" style="left:606px;top:740px">About Pellik</div>
<div class="abs h2" style="left:606px;top:758px">Providing Unique Experiences<br>To Create A Lasting Legacy</div>
<div class="abs rule" style="left:606px;top:860px"></div>
<p class="abs body-text" style="left:606px;top:886px">Lorem ipsum dolor sit amet, consectetuer adipiscing elit, sed diam nonummy nibh euismod tincidunt ut laoreet dolore magna aliquam erat volutpat.</p>
<p class="abs body-text" style="left:606px;top:954px">Ut wisi enim ad minim veniam, quis nostrud exerci tation ullamcorper suscipit lobortis nisl ut aliquip ex ea commodo consequat. Duis autem vel eum iriure dolor in hendrerit in vulputate velit esse moles consequat, vel illum dolore eu feugiat nulla facilisis at vero.</p>
<div class="btn" style="left:606px;top:1063px;width:114px;height:34px">Read More</div>

<!-- SERVICES -->
<div class="abs services" role="img" aria-label="Photo of three business people walking through a bright glass atrium"></div>
<div class="abs" style="left:141px;top:1274px;font-size:13px;font-weight:500;color:var(--ink)">TYPE OF PROPERTY PROJECTS WE DEAL WITH</div>
<div class="abs" style="left:141px;top:1294px;font-size:28px;color:var(--ink)">We take Good Care of Your Property</div>
<div class="abs" style="left:141px;top:1340px;width:56px;height:2px;background:var(--ink)"></div>

<div class="tile" style="left:141px;top:1380px">
  <svg width="66" height="62" fill="none" stroke="var(--green)" stroke-width="2"><path d="M6 28 33 6l27 22M12 24v32h42V24"/><rect x="26" y="36" width="14" height="20"/><path d="M16 32h6v6h-6zM44 32h6v6h-6z"/></svg>
  <p style="top:137px">Leasing</p>
</div>
<div class="tile" style="left:339px;top:1380px">
  <svg width="66" height="62" fill="none" stroke="var(--green)" stroke-width="2"><path d="M14 4h30l10 10v44H14z"/><path d="M44 4v10h10M22 22h22M22 30h22M22 38h14"/><path d="M36 52l16-16 4 4-16 16h-4z"/></svg>
  <p style="top:137px">Projects</p>
</div>
<div class="tile" style="left:141px;top:1572px">
  <svg width="66" height="62" fill="none" stroke="var(--green)" stroke-width="2"><rect x="30" y="4" width="26" height="54"/><path d="M36 12h4M46 12h4M36 22h4M46 22h4M36 32h4M46 32h4M36 42h4M46 42h4"/><rect x="6" y="28" width="24" height="16"/><circle cx="18" cy="36" r="4"/></svg>
  <p style="top:125px">Investments</p>
</div>
<div class="tile" style="left:339px;top:1572px">
  <svg width="66" height="62" fill="none" stroke="var(--green)" stroke-width="2"><path d="M20 24l14-12 14 12v14H20z"/><path d="M6 46c10 0 16 4 24 4h14c4 0 4-6 0-6H32M6 56l14 0 26-4 12-10c2-3-1-6-4-4L44 46"/></svg>
  <p style="top:125px">Property<br>Management</p>
</div>

<!-- PROUD -->
<div class="abs" style="left:0;width:1200px;top:1890px;text-align:center;font-size:31px;line-height:42px;color:var(--ink)">We Are Proud of What We Have Achieved And The<br>Positive Impact We Continue To Make</div>
<div class="abs rule" style="left:571px;top:1992px"></div>

<!-- CAPITAL -->
<svg class="abs" style="left:0;top:2150px" width="600" height="440">
  <polyline points="141,5 110,5 110,429 467,429 467,401" fill="none" stroke="var(--green)" stroke-width="3"/>
</svg>
<div class="photo" style="left:141px;top:2129px;width:381px;height:422px;background:linear-gradient(135deg,#dfe5ea 0%,#a9b3bd 45%,#3a4250 100%)" role="img" aria-label="Photo of three business people talking outside an office building"></div>
<div class="abs h2" style="left:608px;top:2196px;font-size:31px">Capital And Finance</div>
<div class="abs rule" style="left:608px;top:2243px"></div>
<p class="abs body-text" style="left:606px;top:2269px">Lorem ipsum dolor sit amet, consectetuer adipiscing elit, sed diam nonummy nibh euismod tincidunt ut laoreet dolore magna aliquam erat volutpat.</p>
<p class="abs body-text" style="left:606px;top:2337px">Ut wisi enim ad minim veniam, quis nostrud exerci tation ullamcorper suscipit lobortis nisl ut aliquip ex ea commodo consequat. Duis autem vel eum iriure dolor in hendrerit in vulputate velit esse moles consequat, vel illum dolore eu feugiat nulla facilisis at vero.</p>
<div class="btn" style="left:607px;top:2446px;width:127px;height:34px">Know More</div>

<!-- CONTACT -->
<div class="abs" style="left:0;top:2693px;width:1200px;height:545px;background:linear-gradient(180deg,#f1f1f1 0%,#f7f7f7 60%,#fbfbfb 100%)" role="img" aria-label="Photo of a white desk with keyboard, notepad, pencil, coffee cup and plant"></div>
<div class="abs" style="left:0;top:3238px;width:1200px;height:430px;background:var(--dark)"></div>
<div class="abs" style="left:0;top:3483px;width:1200px;height:44px;background:var(--dark-strip)"></div>

<svg class="abs" style="left:268px;top:3300px" width="40" height="42"><path d="M0 6 34 6 34 42Z" fill="var(--green)"/></svg>
<div class="abs" style="left:268px;top:2877px;width:664px;height:465px;background:var(--white);clip-path:polygon(0 0,100% 0,100% 100%,36px 100%,0 427px)"></div>
<div class="abs" style="left:268px;width:664px;top:2943px;text-align:center;font-size:31px;color:var(--ink)">Do You Have A <span style="color:var(--green)">Question?</span></div>
<div class="abs rule" style="left:572px;top:3002px"></div>
<p class="abs" style="left:330px;width:540px;top:3022px;text-align:center;font-size:12.5px;line-height:20px;color:var(--text)">Lorem Ipsum is simply dummy text of the printing and typesetting industry. Lorem Ipsum has been the industry's standard dummy text</p>
<div class="field" style="left:325px;top:3082px;width:268px;height:35px">Name</div>
<div class="field" style="left:607px;top:3082px;width:268px;height:35px">Email</div>
<div class="field" style="left:325px;top:3131px;width:550px;height:84px">Message</div>
<div class="btn" style="left:537px;top:3236px;width:126px;height:35px;font-size:15px">Submit</div>

<!-- FOOTER -->
<div class="abs brand" style="left:0;width:1200px;top:3400px;text-align:center;font-size:44px;letter-spacing:12px">PELLIK</div>
<nav class="footnav">
  <a style="left:358px">Home</a>
  <a style="left:428px">Property</a>
  <a style="left:515px">Capital and finance</a>
  <a style="left:679px">About Us</a>
  <a style="left:769px">Contact Us</a>
</nav>

<div class="info" style="left:148px;top:3567px">Follow Us On</div>
<div class="abs social" style="left:148px;top:3592px"><span></span><span></span><span></span></div>
<div class="divider" style="left:300px"></div>

<svg class="abs" style="left:352px;top:3572px" width="20" height="24" fill="none" stroke="#fff" stroke-width="1.5"><path d="M10 22s7-7 7-12A7 7 0 0 0 3 10c0 5 7 12 7 12z"/><circle cx="10" cy="10" r="2.5"/></svg>
<div class="info" style="left:380px;top:3566px">Pellik<br>Street Name City Name<br>State Zipcode</div>
<div class="divider" style="left:594px"></div>

<svg class="abs" style="left:645px;top:3575px" width="22" height="22" fill="none" stroke="#fff" stroke-width="1.5"><path d="M4 2h4l2 5-3 2a12 12 0 0 0 6 6l2-3 5 2v4a2 2 0 0 1-2 2A18 18 0 0 1 2 4a2 2 0 0 1 2-2z"/></svg>
<div class="info" style="left:682px;top:3576px">Call Us<br>281-555-0142</div>
<div class="divider" style="left:831px"></div>

<svg class="abs" style="left:881px;top:3574px" width="22" height="18" fill="none" stroke="#fff" stroke-width="1.5"><rect x="1" y="3" width="20" height="14"/><path d="M1 3l10 8 10-8"/></svg>
<div class="info" style="left:908px;top:3574px">Email Us<br>inquiry@pellik.com</div>

<div class="abs" style="left:0;top:3668px;width:1200px;height:46px;background:var(--green);color:var(--white);font-size:13px;display:flex;align-items:center;justify-content:center">Copyright © 2019 Pellik. All Rights Reserved.</div>

</body>
</html>
```